Website Design Brief – B2B Industrial Engineering Company

DO NOT CONTACT ME PRIVATELY. ANY INQUIRES WILL BE IGNORED.

1. Industry & Company Background

We are a Swiss B2B engineering and manufacturing company operating in the fields of:
• Industrial air technology (Lufttechnik)
• Metal fabrication and plant construction (Metallbau / Anlagebau)
• Design, fabrication, installation, maintenance, and servicing of:
• Spray booths / paint booths
• Extraction and ventilation systems
• Filtration and environmentally efficient air-handling systems

We plan, build, manufacture, sell, install, and maintain these systems.
Most systems are custom-built in-house (metalwork, apparatus construction, air technology), tailored to customer requirements rather than relying only on standard components.

We are a family-run business with a strong focus on:
• Swiss quality
• Long-term experience
• Reliability and engineering competence
• Environmental efficiency
• Apprenticeship training (we train apprentices in our workshop)

2. Goal of the New Website

The new website should be a modernized evolution of our existing site, not a complete reinvention.

Key objectives:
• Look more modern, fresh, and dynamic
• Clearly communicate our experience, quality, and values
• Emphasize Swiss engineering, tradition, and reliability
• Feel professional and trustworthy, not flashy
• Be clean, uncluttered, and highly structured
• Encourage visitors to submit an inquiry or contact us

The website should feel confident and industrial-premium, with a strong focus on clarity and usability.

3. Overall Design Direction

Visual Style
• Modern industrial design
• Clean layouts with strong structure
• Clear visual hierarchy
• Balanced use of whitespace
• Calm, confident, engineering-focused look

Layout Principles (Important)
• Use clearly separated sections
• Avoid overlapping elements
• Avoid overly complex or experimental layouts
• Prefer grid-based, structured compositions
• Each section should have a clear start and end
• Designs should translate well into standard web layouts without reliance on floating or layered effects

Motion & Media
• A video header on the homepage is strongly desired
• Industrial footage, workshop, fabrication, systems in operation, or environmental technology
• Subtle animations are welcome (e.g., fades, simple transitions)
• Avoid heavy parallax or effects that depend on overlapping elements

4. Target Audience
• Industrial and B2B clients
• Engineers, facility managers, workshop owners
• Decision-makers looking for reliable long-term partners
• Customers who value custom solutions, quality, and service

5. Reference Website

Existing website (content & structure reference):
https://www.glanzhallenwerk.ch

This site:
• Provides existing branding, colors, and tone
• Is the baseline for content and structure
• Should be visually improved, simplified, and modernized

6. Pages to Design (Initial Phase – 5 Pages)

Please design 5 key pages, based on the existing website structure:
1. Home
• Video header
• Clear value proposition
• Overview of services
• Trust elements (experience, Swiss quality, family business)
• Strong call-to-action (Contact / Request Quote)
2. Company / About Us
• Company history
• Values and philosophy
• Swiss quality and tradition
• Family business
• Apprenticeship training and workshop
3. Services / Solutions
• Planning
• Manufacturing
• Installation
• Maintenance & service
• Custom systems vs standard components
4. Products / Systems
• Spray booths
• Extraction systems
• Filtration and air technology
• Modular but clearly structured sections
5. Contact
• Contact form
• Company details
• Location
• Clear inquiry-focused layout

7. Functional Requirements

Must Have
• Contact form
• Newsletter signup
• Cookie consent (EU / GDPR compliant)
• Privacy policy and legal pages (EU data protection)
• Clear navigation structure
• PDF catalog download area (well organized)

Must NOT Have
• No search feature
• No cluttered mega-menus
• No hidden or confusing navigation

8. Future Expansion (Phase Two – Not Required Now)

Designs should allow future expansion, including:
• Multi-language support (English, French, Italian)
• Optional webshop integration
• Expanded product catalog
• Additional service pages

These features do not need to be designed now, but the layout should be flexible enough to support them later.

9. Colors & Branding
• Use colors similar to the existing website
• Industrial, neutral tones preferred
• Accents should feel technical and professional
• Avoid trendy or overly bright color palettes

10. Tone & Messaging

The design should communicate:
• Experience
• Precision
• Trust
• Environmental responsibility
• Custom engineering capability
• Long-term partnership mindset

The overall impression should be:

“A modern Swiss engineering company with deep experience, strong values, and reliable solutions.”

11. Final Notes for Designers
• Focus on clarity, structure, and usability
• Designs should be realistic to implement with standard web layouts
• Avoid designs that rely on overlapping elements or complex layering
• Think in terms of clean sections, strong grids, and clear content flow
• The primary conversion goal is customer inquiries

Target Market(s)

The target market is B2B industrial customers, not consumers.

Industry/Entity Type

B2B industrial engineering and manufacturing (air technology, metal construction, plant engineering).

Number of Pages Required

5+ page

Requirements
Must have
• Clean structured layout, clear B2B positioning, video header, strong inquiry CTA, contact form, GDPR compliance, PDF downloads.
Nice to have
• Newsletter signup, multilingual-ready structure, future webshop support.
Should not have
• Search feature, overlapping elements, complex layered layouts, cluttered navigation.

```html
<!DOCTYPE html>
<html lang="en">
<head>
<meta charset="utf-8">
<title>Glanzhallenwerk AG – Swiss Engineering for Industrial Air</title>
<link rel="stylesheet" href="https://fonts.googleapis.com/css2?family=Montserrat:wght@600;700;800;900&family=Open+Sans:wght@400;600;700&display=swap">
<style>
:root{
  --red:#e2262c;
  --red-dark:#b81c21;
  --ink:#1f1f21;
  --dark:#2a2b2e;
  --darker:#1b1c1e;
  --grey:#6b6d72;
  --light:#f3f3f4;
  --line:#dcdcde;
  --white:#ffffff;
}
*{box-sizing:border-box;margin:0;padding:0}
html,body{width:1200px;height:4276px;overflow:hidden}
body{font-family:"Open Sans",Arial,sans-serif;color:var(--ink);background:var(--white);position:relative}
h1,h2,h3,h4{font-family:"Montserrat",Arial,sans-serif;text-transform:uppercase}
.btn{display:inline-block;font-family:"Montserrat",Arial,sans-serif;font-weight:700;font-size:11px;padding:9px 18px;border-radius:3px;text-decoration:none;white-space:nowrap}
.btn-red{background:var(--red);color:var(--white)}
.btn-outline{border:1.5px solid var(--red);color:var(--red);background:var(--white)}
.btn-outline-light{border:1.5px solid var(--red);color:var(--white)}
.photo{position:absolute}

/* Header */
.site-header{position:absolute;top:0;left:0;width:1200px;height:44px;background:var(--white);box-shadow:0 1px 6px rgba(0,0,0,.08);z-index:5}
.brand{position:absolute;left:40px;top:11px;display:flex;align-items:center;gap:8px;font-family:"Montserrat",Arial,sans-serif;font-weight:800;font-size:14px;color:var(--ink)}
.brand .mark{width:22px;height:22px;background:var(--red)}
.nav{position:absolute;left:530px;top:0;height:44px;display:flex;align-items:center;gap:30px;font-size:12px;font-weight:600}
.nav a{color:var(--ink);text-decoration:none}
.nav a.active{color:var(--red)}
.header-cta{position:absolute;right:40px;top:9px}

/* Hero */
.hero{position:absolute;top:44px;left:0;width:1200px;height:620px;overflow:hidden}
.hero .photo{inset:0;background:linear-gradient(100deg,#2c2d30 0%,#3e4043 40%,#6c6e72 65%,#9a9ca0 85%,#5b5d61 100%)}
.hero h1{position:absolute;left:70px;top:112px;font-weight:900;font-size:42px;line-height:1.08;color:var(--white)}
.hero .lead{position:absolute;left:70px;top:216px;width:440px;font-size:12px;font-weight:700;line-height:1.5;color:var(--white);text-transform:uppercase}
.hero .actions{position:absolute;left:70px;top:348px;display:flex;gap:14px}
.play{position:absolute;left:560px;top:300px}
.hero .cut{position:absolute;left:0;bottom:0}

/* Features */
.features{position:absolute;top:690px;left:112px;width:976px;display:grid;grid-template-columns:repeat(4,1fr);text-align:center}
.feature svg{display:block;margin:0 auto 12px}
.feature h4{font-size:13px;font-weight:800;margin-bottom:6px}
.feature p{font-size:11px;color:var(--grey);line-height:1.45;width:170px;margin:0 auto}

/* Services */
.services-intro{position:absolute;left:112px;top:960px;width:300px}
.services-intro h2{font-size:40px;font-weight:900;line-height:1.05;margin-bottom:16px}
.services-intro p{font-size:11.5px;line-height:1.6;color:var(--grey)}
.service-card{position:absolute;overflow:hidden;border-radius:2px}
.service-card .label{position:absolute;left:18px;bottom:18px;right:18px;color:var(--white)}
.service-card .label h3{font-size:16px;font-weight:800}
.service-card .label p{font-size:10px;margin-top:4px;text-transform:uppercase;font-weight:600}
.service-card .label .bar{width:30px;height:3px;background:var(--red);margin-top:8px}
.service-card.light .label{color:var(--ink)}
.service-card .shade{position:absolute;inset:0;background:linear-gradient(180deg,rgba(0,0,0,0) 50%,rgba(0,0,0,.55) 100%)}

/* About */
.about{position:absolute;top:1710px;left:0;width:1200px;height:430px}
.about .photo{left:0;top:0;width:1200px;height:430px;background:linear-gradient(90deg,#cfd1d3 0%,#8f9296 35%,#3c3e42 65%,#2a2b2e 100%)}
.about-box{position:absolute;left:640px;top:50px;width:440px;height:330px;background:var(--white);padding:36px 40px;box-shadow:0 10px 30px rgba(0,0,0,.2)}
.about-box h2{font-size:38px;font-weight:900;margin-bottom:8px}
.about-box .bar{width:46px;height:4px;background:var(--red);margin-bottom:16px}
.about-box p{font-size:11.5px;line-height:1.65;color:var(--grey);margin-bottom:22px}

/* Products */
.products-head{position:absolute;top:2190px;left:0;width:1200px;text-align:center}
.products-head h2{font-size:40px;font-weight:900}
.products-head p{font-size:11.5px;color:var(--grey);margin-top:6px}
.product-card{position:absolute;top:2300px;width:304px;height:360px;border:1px solid var(--line);background:var(--white);padding:14px}
.product-card .photo{position:relative;height:190px;border-radius:2px}
.product-card h3{font-size:12.5px;font-weight:800;margin-top:14px;line-height:1.35}
.product-card p{font-size:10.5px;color:var(--grey);line-height:1.5;margin-top:6px}
.product-card .actions{position:absolute;left:14px;bottom:16px;display:flex;gap:10px}

/* Eco */
.eco{position:absolute;top:2740px;left:0;width:1200px;height:350px;background:var(--dark);overflow:hidden}
.eco .photo{right:0;top:0;width:640px;height:350px;background:linear-gradient(90deg,#3a3c40 0%,#6f7276 40%,#a4a7ab 75%,#7d8084 100%);clip-path:polygon(12% 0,100% 0,100% 100%,0 100%)}
.eco h2{position:absolute;left:112px;top:60px;font-size:40px;font-weight:900;line-height:1.05;color:var(--white)}
.eco p{position:absolute;left:112px;top:168px;width:400px;font-size:11.5px;line-height:1.6;color:#c7c8cb}
.eco .btn{position:absolute;left:112px;top:262px}

/* GDPR */
.gdpr-list{position:absolute;left:112px;top:3140px;width:390px;display:flex;flex-direction:column;gap:18px}
.gdpr-item{display:flex;align-items:center;gap:16px;border:1.5px solid var(--red);padding:12px 16px;border-radius:2px;box-shadow:6px 6px 0 rgba(226,38,44,.12)}
.gdpr-item .icon{width:40px;height:40px;background:var(--red);display:flex;align-items:center;justify-content:center;flex:none}
.gdpr-item span{font-family:"Montserrat",Arial,sans-serif;font-weight:800;font-size:12px;text-transform:uppercase;line-height:1.35}
.gdpr-text{position:absolute;left:640px;top:3200px;width:440px}
.gdpr-text h2{font-size:40px;font-weight:900;margin-bottom:14px}
.gdpr-text p{font-size:11.5px;line-height:1.65;color:var(--grey);margin-bottom:22px}
.gdpr-text .actions{display:flex;gap:14px}

/* CTA */
.cta{position:absolute;top:3540px;left:0;width:1200px;height:320px;background:var(--darker);overflow:hidden}
.cta .texture{position:absolute;inset:0;background:linear-gradient(115deg,#2c2d30 0%,#1b1c1e 60%,#25262a 100%)}
.cta h2{position:absolute;left:112px;top:52px;font-size:38px;font-weight:900;line-height:1.08;color:var(--white)}
.cta p{position:absolute;left:112px;top:150px;width:400px;font-size:11.5px;line-height:1.6;color:#c7c8cb}
.cta .btn{position:absolute;left:112px;top:222px}
.inquiry{position:absolute;left:680px;top:3500px;width:380px;height:360px;background:var(--white);border:1px solid var(--line);box-shadow:0 12px 30px rgba(0,0,0,.25);padding:24px 26px;z-index:2}
.inquiry h4{font-size:15px;font-weight:800;text-align:center;margin-bottom:16px}
.inquiry .row{display:grid;grid-template-columns:1fr 1fr;gap:10px;margin-bottom:10px}
.field{border:1px solid var(--line);height:32px;font-size:10.5px;color:#9a9ca0;padding:9px 10px}
.field.area{height:90px;margin-bottom:14px}

/* Footer */
.footer{position:absolute;top:3860px;left:0;width:1200px;height:416px;background:#19191b;color:#bdbec2}
.footer .col{position:absolute;top:60px}
.footer .brand-foot{display:flex;align-items:center;gap:8px;font-family:"Montserrat",Arial,sans-serif;font-weight:800;font-size:15px;color:var(--white);margin-bottom:18px}
.footer .brand-foot .mark{width:22px;height:22px;background:var(--red)}
.footer p{font-size:11px;line-height:1.65}
.footer h4{font-size:13px;font-weight:800;color:var(--white);margin-bottom:14px}
.footer ul{list-style:none;font-size:11px;line-height:2}
.footer .contact-line{display:flex;gap:8px;align-items:flex-start;font-size:11px;line-height:1.55;margin-bottom:10px}
.socials{display:flex;gap:10px;margin-top:20px}
.socials span{width:14px;height:14px;border-radius:50%;background:#5b5c60}
.news-field{margin-top:14px;height:32px;background:var(--white);font-size:10.5px;color:#9a9ca0;padding:9px 10px;width:220px}
.footer .btn{margin-top:12px}
.copyright{position:absolute;left:112px;right:112px;top:350px;border-top:1px solid #333437;padding-top:18px;text-align:center;font-size:10.5px;color:#8b8c90}
</style>
</head>
<body>

<header class="site-header">
  <div class="brand"><span class="mark"></span>GLANZHALLENWERK AG</div>
  <nav class="nav">
    <a class="active" href="#">Home</a><a href="#">About Us</a><a href="#">Services</a><a href="#">Products</a><a href="#">Contact</a>
  </nav>
  <a class="btn btn-red header-cta" href="#">Request a Quote →</a>
</header>

<section class="hero">
  <div class="photo" role="img" aria-label="Video header: worker in protective suit spray-painting inside an industrial paint booth"></div>
  <h1>Swiss Engineering<br>for Industrial Air</h1>
  <p class="lead">Custom-built spray booths, extraction systems and air-handling solutions — planned, manufactured and serviced in Switzerland.</p>
  <div class="actions">
    <a class="btn btn-red" href="#">Request a Quote →</a>
    <a class="btn btn-outline-light" href="#">Contact Us →</a>
  </div>
  <svg class="play" width="70" height="70" viewBox="0 0 70 70"><circle cx="35" cy="35" r="33" fill="rgba(255,255,255,.25)" stroke="#fff" stroke-width="2"/><path d="M28 22 L50 35 L28 48Z" fill="#fff"/></svg>
  <svg class="cut" width="1200" height="110" viewBox="0 0 1200 110"><path d="M0 70 L900 40 L1200 95 L1200 110 L0 110Z" fill="#fff"/><path d="M0 62 L900 32 L1200 87" fill="none" stroke="#e2262c" stroke-width="5"/></svg>
</section>

<section class="features">
  <div class="feature">
    <svg width="36" height="36" viewBox="0 0 36 36"><path d="M18 3 L31 8 V18 C31 26 25 31 18 33 C11 31 5 26 5 18 V8Z" fill="none" stroke="#e2262c" stroke-width="2.5"/><path d="M12 18 L16 22 L24 13" fill="none" stroke="#e2262c" stroke-width="2.5"/></svg>
    <h4>Swiss Quality</h4><p>Engineered, manufactured and tested in Switzerland.</p>
  </div>
  <div class="feature">
    <svg width="36" height="36" viewBox="0 0 36 36"><circle cx="18" cy="18" r="7" fill="none" stroke="#e2262c" stroke-width="2.5"/><path d="M18 3v6M18 27v6M3 18h6M27 18h6M7 7l4 4M25 25l4 4M7 29l4-4M25 11l4-4" stroke="#e2262c" stroke-width="2.5"/></svg>
    <h4>Custom Solutions</h4><p>Engineered to match your process and environment.</p>
  </div>
  <div class="feature">
    <svg width="36" height="36" viewBox="0 0 36 36"><circle cx="18" cy="15" r="11" fill="none" stroke="#e2262c" stroke-width="2.5"/><path d="M13 15 L17 19 L24 11" fill="none" stroke="#e2262c" stroke-width="2.5"/><path d="M12 24 L10 34 L18 30 L26 34 L24 24" fill="none" stroke="#e2262c" stroke-width="2.5"/></svg>
    <h4>Industrial Standards</h4><p>Built to recognised industry standards.</p>
  </div>
  <div class="feature">
    <svg width="36" height="36" viewBox="0 0 36 36"><path d="M6 32h24M10 32V20M17 32V14M24 32V8" stroke="#e2262c" stroke-width="3"/><path d="M8 14 L16 8 L22 11 L30 4" fill="none" stroke="#e2262c" stroke-width="2.5"/></svg>
    <h4>Sustainability</h4><p>Efficient systems aligned with environmental standards.</p>
  </div>
</section>

<section class="services">
  <div class="services-intro">
    <h2>Our<br>Services</h2>
    <p>Our services cover planning, manufacturing, installation and maintenance of industrial air systems. With our own workshop, we deliver consistent quality, efficient project execution and dependable long-term support.</p>
  </div>
  <div class="service-card light" style="left:440px;top:920px;width:320px;height:320px">
    <div class="photo" role="img" aria-label="Engineer's hand drawing technical plans at a desk" style="inset:0;background:linear-gradient(160deg,#f4f4f5 0%,#d9dadc 55%,#b9bbbe 100%)"></div>
    <div class="label"><h3>Planning</h3><div class="bar"></div></div>
  </div>
  <div class="service-card" style="left:780px;top:920px;width:300px;height:320px">
    <div class="photo" role="img" aria-label="Welder fabricating metal parts in the workshop" style="inset:0;background:linear-gradient(160deg,#55575b 0%,#3a3b3f 60%,#2a2b2e 100%)"></div>
    <div class="shade"></div>
    <div class="label"><h3>Manufacturing</h3><p>In-house metalwork for custom industrial systems</p><div class="bar"></div></div>
  </div>
  <div class="service-card" style="left:112px;top:1280px;width:308px;height:360px">
    <div class="photo" role="img" aria-label="Technician in hard hat installing a system with a tablet" style="inset:0;background:linear-gradient(160deg,#d8c8a8 0%,#9c9478 45%,#5a5a58 100%)"></div>
    <div class="shade"></div>
    <div class="label"><h3>Installation</h3><div class="bar"></div></div>
  </div>
  <div class="service-card" style="left:440px;top:1280px;width:320px;height:360px">
    <div class="photo" role="img" aria-label="Service technician inspecting ventilation equipment" style="inset:0;background:linear-gradient(160deg,#b5b7ba 0%,#7f8286 50%,#4c4e52 100%)"></div>
    <div class="shade"></div>
    <div class="label"><h3>Maintenance &amp; Service</h3><div class="bar"></div></div>
  </div>
  <div class="service-card" style="left:780px;top:1280px;width:300px;height:360px">
    <div class="photo" role="img" aria-label="Engineering team reviewing plans in a meeting" style="inset:0;background:linear-gradient(160deg,#e6e2dc 0%,#b6b0a7 50%,#6a6660 100%)"></div>
    <div class="shade"></div>
    <div class="label"><h3>Custom Systems vs<br>Standard Components</h3><div class="bar"></div></div>
  </div>
</section>

<section class="about">
  <div class="photo" role="img" aria-label="Worker in protective suit spraying in a white paint booth"></div>
  <div class="about-box">
    <h2>About Us</h2>
    <div class="bar"></div>
    <p>We are a family-run Swiss engineering and manufacturing company specializing in industrial air technology, metal construction and plant engineering. With decades of experience, we design, build and maintain custom systems that meet the highest standards of quality, reliability and efficiency.</p>
    <a class="btn btn-red" href="#">Learn More →</a>
  </div>
</section>

<div class="products-head">
  <h2>Our Products</h2>
  <p>Extraction, filtration, heating, cooling efficiency and quality</p>
</div>
<article class="product-card" style="left:120px">
  <div class="photo" role="img" aria-label="Modular paint booth cabin interior" style="background:linear-gradient(180deg,#e9eaec 0%,#c4c7cb 60%,#9ea2a7 100%)"></div>
  <h3>AeroLine Cabin<br>Modular Paint Booth</h3>
  <p>A modular paint booth for efficient, clean coating work.</p>
  <div class="actions"><a class="btn btn-red" href="#">Learn More →</a><a class="btn btn-outline" href="#">Download PDF ↓</a></div>
</article>
<article class="product-card" style="left:448px">
  <div class="photo" role="img" aria-label="Extraction wall with splash panel" style="background:linear-gradient(180deg,#dfe6ee 0%,#9fb3c9 55%,#6e86a2 100%)"></div>
  <h3>Extraction Wall<br>Splash Wall</h3>
  <p>Reliable overspray extraction for workshops of every size.</p>
  <div class="actions"><a class="btn btn-red" href="#">Learn More →</a><a class="btn btn-outline" href="#">Download PDF ↓</a></div>
</article>
<article class="product-card" style="left:780px">
  <div class="photo" role="img" aria-label="Assorted filter mats and cassettes" style="background:linear-gradient(135deg,#c9d9a6 0%,#d8c49a 45%,#9a9c9f 100%)"></div>
  <h3>Filter Technology<br>Affordable Filters from Stock</h3>
  <p>Quality filter media available directly from our stock.</p>
  <div class="actions"><a class="btn btn-red" href="#">Learn More →</a><a class="btn btn-outline" href="#">Download PDF ↓</a></div>
</article>

<section class="eco">
  <div class="photo" role="img" aria-label="Painter in respirator mask spraying a vehicle part"></div>
  <h2>Eco-Efficient Air<br>Technology</h2>
  <p>We develop air-handling and filtration systems that combine operational efficiency with environmental responsibility. All components are optimised for energy savings and low emissions.</p>
  <a class="btn btn-red" href="#">Learn More →</a>
</section>

<section class="gdpr">
  <div class="gdpr-list">
    <div class="gdpr-item"><div class="icon"><svg width="20" height="20" viewBox="0 0 20 20"><path d="M4 10l4 4 8-9" fill="none" stroke="#fff" stroke-width="2.5"/></svg></div><span>Personal data collected only<br>as necessary</span></div>
    <div class="gdpr-item"><div class="icon"><svg width="20" height="20" viewBox="0 0 20 20"><rect x="4" y="9" width="12" height="9" fill="#fff"/><path d="M7 9V6a3 3 0 0 1 6 0v3" fill="none" stroke="#fff" stroke-width="2"/></svg></div><span>Secure storage and lawful<br>processing</span></div>
    <div class="gdpr-item"><div class="icon"><svg width="20" height="20" viewBox="0 0 20 20"><circle cx="10" cy="7" r="4" fill="#fff"/><path d="M3 18c1-4 4-6 7-6s6 2 7 6" fill="#fff"/></svg></div><span>User rights: access, correction,<br>deletion</span></div>
    <div class="gdpr-item"><div class="icon"><svg width="20" height="20" viewBox="0 0 20 20"><rect x="3" y="5" width="14" height="10" fill="none" stroke="#fff" stroke-width="2"/><path d="M3 5l7 6 7-6" fill="none" stroke="#fff" stroke-width="2"/></svg></div><span>Optional note on email /<br>newsletter GDPR compliance</span></div>
  </div>
  <div class="gdpr-text">
    <h2>GDPR Compliance</h2>
    <p>We process personal data lawfully and in full compliance with the EU General Data Protection Regulation (GDPR). Data is collected only where necessary, stored securely, and used exclusively for its intended purpose.</p>
    <div class="actions"><a class="btn btn-red" href="#">Privacy Policy →</a><a class="btn btn-outline" href="#">Cookie Settings →</a></div>
  </div>
</section>

<section class="cta">
  <div class="texture"></div>
  <h2>From Concept to<br>Long-Term Operation</h2>
  <p>Your experienced partner for planning, manufacturing, installation and maintenance of industrial air and plant systems.</p>
  <a class="btn btn-red" href="#">Contact Us →</a>
</section>
<form class="inquiry">
  <h4>Project Inquiry</h4>
  <div class="row"><div class="field">First Name</div><div class="field">Last Name</div></div>
  <div class="row"><div class="field">Email</div><div class="field">Phone Number</div></div>
  <div class="field area">Message...</div>
  <a class="btn btn-red" href="#">Submit →</a>
</form>

<footer class="footer">
  <div class="col" style="left:112px;width:230px">
    <div class="brand-foot"><span class="mark"></span>GLANZHALLENWERK AG</div>
    <p>We create innovative solutions that benefit from our experience in plant engineering for surface technology.</p>
    <div class="socials"><span></span><span></span><span></span></div>
  </div>
  <div class="col" style="left:400px">
    <h4>Navigation</h4>
    <ul><li>Home</li><li>About Us</li><li>Services</li><li>Products</li><li>Contact Us</li></ul>
  </div>
  <div class="col" style="left:580px;width:230px">
    <h4>Contact Us</h4>
    <div class="contact-line"><svg width="12" height="14" viewBox="0 0 12 14"><path d="M6 0a5 5 0 0 1 5 5c0 4-5 9-5 9S1 9 1 5a5 5 0 0 1 5-5z" fill="#e2262c"/><circle cx="6" cy="5" r="2" fill="#19191b"/></svg><span>Werkstrasse 14, 8500 Frauenfeld</span></div>
    <div class="contact-line"><svg width="12" height="12" viewBox="0 0 12 12"><path d="M2 0h3l1 3-2 1.5a7 7 0 0 0 3.5 3.5L9 6l3 1v3c0 1-1 2-2 2C4.5 12 0 7.5 0 2 0 1 1 0 2 0z" fill="#e2262c"/></svg><span>+41 52 714 28 60<br>Mon–Thu 07:00–17:00<br>Fri 07:00–16:00</span></div>
    <div class="contact-line"><svg width="12" height="10" viewBox="0 0 12 10"><rect width="12" height="10" fill="#e2262c"/><path d="M0 0l6 5 6-5" fill="none" stroke="#19191b" stroke-width="1.2"/></svg><span>info@glanzhallenwerk.ch</span></div>
  </div>
  <div class="col" style="left:860px;width:230px">
    <h4>Newsletter</h4>
    <p>Engineering updates, project insights and company news.</p>
    <div class="news-field">Email Address</div>
    <a class="btn btn-red" href="#">Subscribe →</a>
  </div>
  <div class="copyright">© 2026 Glanzhallenwerk AG. All rights reserved.</div>
</footer>

</body>
</html>
```